Tamsworth Counsel Cover 3 - Capital Allocation battlefield

Tamsworth Counsel is a business consulting firm. We will publish a series of four thought leadership pieces online and via PDF. The third of the series is attached to this project. We need an eye-catching cover page with a back page that keeps with our branding. The document attached is in the final draft, and the cover and pack pages are placeholders only. You can find more about our branding and style on our website www.tamsworthcounsel.com.au. The other three projects can be found here with a similar brief, and you are welcome to submit a design for all 4.

```html
<!DOCTYPE html>
<html lang="en">
<head>
<meta charset="utf-8">
<title>Tamsworth Counsel – The Capital Allocation Battlefield</title>
<link href="https://fonts.googleapis.com/css2?family=Poppins:wght@400;500;600;700&display=swap" rel="stylesheet">
<style>
  :root {
    --stage: #a4a4a4;
    --paper: #f0f1f3;
    --paper-back: #dfe3e7;
    --paper-shade: #e3e6ea;
    --sky: #12a6e6;
    --orange: #f7931e;
    --ink: #2e3a46;
    --ink-soft: #3d4852;
    --white: #ffffff;
  }
  * { margin: 0; padding: 0; box-sizing: border-box; }
  html, body {
    width: 1200px; height: 847px; overflow: hidden;
    background: var(--stage);
    font-family: "Poppins", sans-serif;
  }
  .spread { position: relative; width: 1200px; height: 847px; }
  .page {
    position: absolute; top: 27px; width: 560px; height: 793px;
    overflow: hidden;
  }
  .page--cover { left: 27px; background: var(--paper); }
  .page--back { left: 613px; background: var(--paper-back); }
  .page-art { position: absolute; inset: 0; width: 560px; height: 793px; }

  .brand {
    position: absolute; display: flex; align-items: center; gap: 10px;
    color: var(--ink); font-weight: 600; line-height: 1.05;
  }
  .brand__dot { border-radius: 50%; background: var(--orange); flex: none; }
  .brand--cover { left: 40px; top: 40px; font-size: 19px; }
  .brand--cover .brand__dot { width: 40px; height: 40px; }
  .brand--back { left: 40px; top: 40px; font-size: 29px; }
  .brand--back .brand__dot { width: 62px; height: 62px; }

  .cover-title {
    position: absolute; left: 40px; top: 136px;
    color: var(--sky); font-weight: 700; font-size: 45px; line-height: 55px;
    letter-spacing: 0.2px;
  }
  .cover-subtitle {
    position: absolute; left: 40px; top: 298px;
    color: var(--ink); font-weight: 500; font-size: 18px;
  }

  .web-link {
    position: absolute; display: flex; align-items: center; gap: 7px;
    font-weight: 500; font-size: 15px;
  }
  .web-link svg { width: 14px; height: 14px; }
  .page--cover .web-link { left: 250px; top: 758px; color: var(--ink); }
  .page--back .web-link { left: 287px; top: 758px; color: var(--white); }

  .contact-heading {
    position: absolute; left: 40px; top: 170px;
    color: var(--orange); font-weight: 600; font-size: 35px;
  }
  .contact-intro {
    position: absolute; left: 40px; top: 228px;
    color: var(--ink); font-weight: 500; font-size: 21px; line-height: 27px;
  }
  .contact-intro strong { font-weight: 700; }
  .person { position: absolute; left: 40px; color: var(--ink-soft); }
  .person--one { top: 330px; }
  .person--two { top: 437px; }
  .person__name { color: var(--orange); font-weight: 600; font-size: 22px; line-height: 30px; }
  .person__role { color: var(--sky); font-weight: 600; font-size: 12.5px; line-height: 16px; margin-bottom: 8px; }
  .person__line { font-size: 13px; line-height: 17px; }

  .follow {
    position: absolute; left: 40px; top: 778px; transform: translateY(-50%);
    display: flex; align-items: center; gap: 10px;
    color: var(--ink); font-weight: 600; font-size: 12px;
  }
  .follow__icon { width: 14px; height: 14px; border-radius: 2px; background: var(--ink); }
  .follow__icon + .follow__icon { margin-left: 4px; }
</style>
</head>
<body>
<main class="spread">

  <section class="page page--cover">
    <svg class="page-art" viewBox="0 0 420 595" preserveAspectRatio="none" aria-hidden="true">
      <defs>
        <linearGradient id="towerWarm" x1="0" y1="0" x2="1" y2="1">
          <stop offset="0" stop-color="#e6b684"/>
          <stop offset="0.55" stop-color="#b07a45"/>
          <stop offset="1" stop-color="#4a321c"/>
        </linearGradient>
        <linearGradient id="towerCool" x1="1" y1="0" x2="0" y2="1">
          <stop offset="0" stop-color="#6cc8ee"/>
          <stop offset="0.5" stop-color="#1f7fb5"/>
          <stop offset="1" stop-color="#0b4a70"/>
        </linearGradient>
      </defs>
      <polygon points="0,595 0,470 210,595" fill="var(--paper-shade)"/>
      <polygon points="420,330 420,595 250,595" fill="var(--paper-shade)"/>
      <polygon points="0,160 0,248 150,248 420,120 420,100" fill="#e9ebee"/>
      <rect x="150" y="247" width="270" height="83" fill="var(--sky)"/>
      <rect x="150" y="368" width="160" height="78" fill="var(--orange)"/>
      <polygon points="0,250 130,250 215,345 0,528" fill="url(#towerWarm)" role="img" aria-label="Photo of a warm-toned office tower facade"/>
      <polygon points="218,342 420,145 420,446 318,446" fill="url(#towerCool)" role="img" aria-label="Photo of a blue glass skyscraper"/>
      <line x1="-5" y1="570" x2="430" y2="135" stroke="var(--white)" stroke-width="13"/>
      <line x1="128" y1="246" x2="345" y2="470" stroke="var(--white)" stroke-width="13"/>
    </svg>

    <div class="brand brand--cover"><span class="brand__dot"></span><span>Tamsworth<br>Counsel</span></div>
    <h1 class="cover-title">The Capital<br>Allocation<br>Battlefield</h1>
    <p class="cover-subtitle">Deploying the War Chest</p>

    <div class="web-link">
      <svg viewBox="0 0 16 16" aria-hidden="true"><g fill="none" stroke="currentColor" stroke-width="1.5"><circle cx="8" cy="8" r="6.5"/><ellipse cx="8" cy="8" rx="3" ry="6.5"/><line x1="1.5" y1="8" x2="14.5" y2="8"/></g></svg>
      <span>tamsworthcounsel.com.au</span>
    </div>
  </section>

  <section class="page page--back">
    <svg class="page-art" viewBox="0 0 420 595" preserveAspectRatio="none" aria-hidden="true">
      <polygon points="0,0 58,0 0,150" fill="var(--sky)"/>
      <polygon points="295,90 420,90 420,50 322,50" fill="var(--sky)"/>
      <polygon points="315,80 420,80 420,38 342,38" fill="var(--orange)"/>
      <polygon points="420,110 420,125 155,595 138,595" fill="var(--white)"/>
      <polygon points="420,132 420,595 160,595" fill="var(--orange)"/>
    </svg>

    <div class="brand brand--back"><span class="brand__dot"></span><span>Tamsworth<br>Counsel</span></div>

    <h2 class="contact-heading">Contact us</h2>
    <p class="contact-intro">Find out how <strong>Tamsworth Counsel</strong><br>can help build your company<br>into a market leader today.</p>

    <div class="person person--one">
      <p class="person__name">Edmund Tamsworth</p>
      <p class="person__role">Managing Director</p>
      <p class="person__line">Mobile: +61 400 318 226</p>
      <p class="person__line">Email: edmund@tamsworthcounsel.com.au</p>
    </div>
    <div class="person person--two">
      <p class="person__name">Miles Tamsworth</p>
      <p class="person__role">Managing Director</p>
      <p class="person__line">Mobile: +61 400 562 907</p>
      <p class="person__line">Email: miles@tamsworthcounsel.com.au</p>
    </div>

    <div class="follow">
      <span>Follow us</span>
      <span class="follow__icon" aria-label="Social profile one"></span>
      <span class="follow__icon" aria-label="Social profile two"></span>
    </div>

    <div class="web-link">
      <svg viewBox="0 0 16 16" aria-hidden="true"><g fill="none" stroke="currentColor" stroke-width="1.5"><circle cx="8" cy="8" r="6.5"/><ellipse cx="8" cy="8" rx="3" ry="6.5"/><line x1="1.5" y1="8" x2="14.5" y2="8"/></g></svg>
      <span>tamsworthcounsel.com.au</span>
    </div>
  </section>

</main>
</body>
</html>
```